Business Card for Managing Partner Investment Fund

To create a business card template for an investment fund manager. Business card should be more professional in nature, not too colorful, more upscale, and created using the attached logos and fund name files. I would prefer a black or gray color scheme, but am open to the use of color as well. I would prefer a double sided business card, but open to single sided business card designs as well. The business card should include: name, title, and contact information, as well as logo and company name. I would prefer a more stream-lined, simple business card design.
Updates
Address: 4190 NE 38th Ter. Ocala, FL 34470
Email: talvin47@quorimail.net
Phone: 561-347-9162
Title: managing partner
Name: Dorian Velsky
Fund Name: Ambergate Capital
Logos can be found in files attached to the brief
Target Market(s)
potential investors, other fund managers
Industry/Entity Type
Finance
Contact Information for Business Card
Name on card: Dorian Velsky
Title: Managing Partner
Colors
Designer to choose colors to be used in the design.
Requirements
Must have
- Phone number
- email address
- physical address
- title
- name
- logo
- Fund name
Nice to have
- simple layout
Should not have
- too many colors, busy fonts,

```html
<!DOCTYPE html>
<html lang="en">
<head>
<meta charset="utf-8">
<title>Ambergate Capital – Business Card</title>
<link href="https://fonts.googleapis.com/css2?family=Work+Sans:wght@400;500;700&display=swap" rel="stylesheet">
<style>
  :root {
    --stage: #262626;
    --card: #ffffff;
    --ink: #111111;
    --ink-soft: #2b2b2b;
    --rule: #444444;
  }
  html, body {
    margin: 0;
    padding: 0;
    width: 1200px;
    height: 1000px;
    overflow: hidden;
    background: var(--stage);
    font-family: "Work Sans", Arial, sans-serif;
  }
  .canvas {
    position: relative;
    width: 1200px;
    height: 1000px;
  }
  .card {
    position: absolute;
    width: 560px;
    height: 320px;
    background: var(--card);
    border-radius: 30px;
    box-sizing: border-box;
  }
  .card--front { left: 110px; top: 110px; }
  .card--back  { left: 530px; top: 570px; }

  /* Front: company name */
  .brand {
    position: absolute;
    left: 0; right: 0; top: 50%;
    transform: translateY(-50%);
    text-align: center;
    color: var(--ink);
  }
  .brand__name {
    display: inline-flex;
    align-items: center;
    gap: 14px;
    font-size: 34px;
    font-weight: 500;
    letter-spacing: 0.12em;
    text-transform: uppercase;
  }
  .brand__mark {
    width: 18px;
    height: 18px;
    background: var(--ink);
  }
  .brand__rule {
    width: 300px;
    height: 1px;
    background: var(--rule);
    margin: 16px auto 0;
  }

  /* Back: identity + contact */
  .identity {
    position: absolute;
    left: 44px;
    top: 70px;
    color: var(--ink);
  }
  .identity__name {
    margin: 0;
    font-size: 25px;
    font-weight: 700;
    letter-spacing: 0.03em;
    text-transform: uppercase;
  }
  .identity__title {
    margin: 4px 0 0 14px;
    font-size: 11px;
    font-weight: 500;
    letter-spacing: 0.04em;
    text-transform: uppercase;
  }
  .contact {
    position: absolute;
    left: 44px;
    bottom: 40px;
    margin: 0;
    padding: 0;
    list-style: none;
    color: var(--ink-soft);
    font-size: 14px;
    line-height: 24px;
  }
  .contact__item {
    display: flex;
    align-items: center;
    gap: 8px;
  }
  .contact__icon { width: 12px; height: 12px; flex: none; }
  .contact__item--plain { padding-left: 0; }

  .back-brand {
    position: absolute;
    right: 36px;
    top: 110px;
    display: flex;
    align-items: center;
    gap: 10px;
    color: var(--ink);
    font-size: 17px;
    font-weight: 500;
    letter-spacing: 0.12em;
    text-transform: uppercase;
  }
  .back-brand__mark {
    width: 12px;
    height: 12px;
    background: var(--ink);
  }
</style>
</head>
<body>
<main class="canvas">

  <section class="card card--front" aria-label="Card front">
    <div class="brand">
      <div class="brand__name"><span class="brand__mark"></span>Ambergate Capital</div>
      <div class="brand__rule"></div>
    </div>
  </section>

  <section class="card card--back" aria-label="Card back">
    <div class="identity">
      <h1 class="identity__name">Dorian Velsky</h1>
      <p class="identity__title">Managing Partner</p>
    </div>

    <div class="back-brand"><span class="back-brand__mark"></span>Ambergate Capital</div>

    <ul class="contact">
      <li class="contact__item">
        <svg class="contact__icon" viewBox="0 0 12 12" aria-hidden="true">
          <rect x="3" y="0.5" width="6" height="11" rx="1.2" fill="none" stroke="#111" stroke-width="1.2"/>
          <line x1="5" y1="9.5" x2="7" y2="9.5" stroke="#111" stroke-width="1"/>
        </svg>
        561-347-9162
      </li>
      <li class="contact__item">
        <svg class="contact__icon" viewBox="0 0 12 12" aria-hidden="true">
          <rect x="0.5" y="2" width="11" height="8" fill="#111"/>
          <polyline points="0.5,2 6,6.5 11.5,2" fill="none" stroke="#fff" stroke-width="1"/>
        </svg>
        talvin47@quorimail.net
      </li>
      <li class="contact__item contact__item--plain">4190 NE 38th Ter. Ocala, FL 34470</li>
    </ul>
  </section>

</main>
</body>
</html>
```